HUSH: Hush Until Stories Happen school library event

I need two poster designs for Hush Until Stories Happen (HUSH) in BC, requested by the PCSMG--Pacific Coast School Media Guild. One should be for elementary students and one for high school. I want the date (Monday, October 26, 2020) and Hush Until Stories Happen. I would like the posters in English and in French. French is : Ferme Ton Écran Maintenant! I'm including last year's posters as examples. I would like to be able to print the poster files on 11x17 paper.

• -The phrase "Hush Until Stories Happen" for the English version; "Ferme Ton Écran Maintenant" for the French version.
-Include the organization name: Pacific Coast School Media Guild
-The date: Monday, October 26, 2020
• I would like the elementary version to be bright and colourful--fun for younger kids. I would like the high school version to be a bit more mature for the older students. Can still be bright and colourful.

```html
<!DOCTYPE html>
<html lang="en">
<head>
<meta charset="utf-8">
<title>HUSH — Hush Until Stories Happen</title>
<link rel="stylesheet" href="https://fonts.googleapis.com/css2?family=Bungee&family=Montserrat:wght@400;500;800&family=Rubik+Mono+One&display=swap">
<style>
  :root {
    --sun: #F6D136;
    --sky: #7ACCDB;
    --ink: #3A3A3C;
  }
  html, body {
    margin: 0;
    padding: 0;
    width: 777px;
    height: 1200px;
    overflow: hidden;
    background: var(--sun);
  }
  .poster {
    position: relative;
    width: 777px;
    height: 1200px;
    background: var(--sun);
    font-family: "Montserrat", sans-serif;
    color: var(--ink);
  }
  .org-name {
    position: absolute;
    top: 148px;
    left: 0;
    width: 100%;
    margin: 0;
    text-align: center;
    font-weight: 400;
    font-size: 22px;
    line-height: 31px;
    letter-spacing: 0.12em;
    text-transform: uppercase;
  }
  .org-name .highlight {
    background: var(--sky);
    padding: 0 2px 0 4px;
  }
  .headline-art {
    position: absolute;
    top: 0;
    left: 0;
    width: 777px;
    height: 1200px;
  }
  .word-hush {
    font-family: "Rubik Mono One", sans-serif;
    fill: var(--ink);
  }
  .word-connector {
    font-family: "Montserrat", sans-serif;
    fill: var(--ink);
  }
  .word-connector .bold { font-weight: 800; }
  .word-connector .regular { font-weight: 400; }
  .rule { stroke: var(--ink); stroke-width: 2; }
  .word-happen {
    font-family: "Bungee", sans-serif;
  }
  .event-date {
    position: absolute;
    top: 1040px;
    left: 0;
    width: 100%;
    margin: 0;
    text-align: center;
    font-weight: 500;
    font-size: 25px;
    letter-spacing: 0.13em;
  }
</style>
</head>
<body>
<main class="poster">
  <h2 class="org-name">
    Pacific Coast <span class="highlight">School</span><br>
    <span class="highlight">Media</span> Guild
  </h2>

  <svg class="headline-art" viewBox="0 0 777 1200" role="img" aria-label="Hush Until Stories Happen">
    <defs>
      <path id="half-disc" d="M624.6 295.4 A360 360 0 0 1 115.4 804.6 Z"/>
      <clipPath id="sky-clip"><use href="#half-disc"/></clipPath>
      <text id="happen-face" class="word-happen" x="126" y="738" font-size="180" textLength="542" lengthAdjust="spacingAndGlyphs">HAPPEN</text>
    </defs>

    <use class="backdrop-disc" href="#half-disc" fill="var(--sky)"/>

    <text class="word-hush" x="112" y="528" font-size="205" textLength="556" lengthAdjust="spacingAndGlyphs">HUSH</text>

    <line class="rule" x1="68" y1="570" x2="172" y2="570"/>
    <text class="word-connector" x="180" y="582" font-size="41" textLength="402" lengthAdjust="spacingAndGlyphs"><tspan class="bold">UNTIL STORIES</tspan></text>
    <line class="rule" x1="588" y1="570" x2="694" y2="570"/>

    <g class="happen-extrusion" fill="var(--ink)">
      <use href="#happen-face" x="-16" y="18"/>
      <use href="#happen-face" x="-14" y="16"/>
      <use href="#happen-face" x="-12" y="14"/>
      <use href="#happen-face" x="-10" y="12"/>
      <use href="#happen-face" x="-8" y="9"/>
      <use href="#happen-face" x="-6" y="7"/>
      <use href="#happen-face" x="-4" y="5"/>
      <use href="#happen-face" x="-2" y="2"/>
    </g>
    <use class="happen-face-sun" href="#happen-face" fill="var(--sun)"/>
    <use class="happen-face-sky" href="#happen-face" fill="var(--sky)" clip-path="url(#sky-clip)"/>
    <use class="happen-outline" href="#happen-face" fill="none" stroke="var(--ink)" stroke-width="1.6"/>
  </svg>

  <p class="event-date">Monday, October 26, 2020</p>
</main>
</body>
</html>
```